IT Company based on Biology Business Needs a Business Card Design

We need a business card design for a new company called 'Lumen CELL'. We develop the machine learning solutions especially focused on deep learning algorithms for biology industry. Our initial product is a vision detection on biological images to help doctors diagnose the symptoms. We would like to see designs that use the color green.

Industry/Entity Type

Business

```html
<!DOCTYPE html>
<html lang="en">
<head>
<meta charset="utf-8">
<title>Lumen CELL – Business Card</title>
<link href="https://fonts.googleapis.com/css2?family=Lato:wght@400;700&display=swap" rel="stylesheet">
<style>
  :root {
    --backdrop: #e9e6e2;
    --card-dark: #0d1513;
    --card-dark-edge: #070b0a;
    --brand-green: #a9dc6c;
    --strand-green: #4fae4a;
    --strand-grey: #3a3f3d;
    --name-green: #2bb878;
    --name-green-deep: #22a86a;
    --contact-light: #a6d972;
    --contact-deep: #55a62a;
    --ink: #0f1a14;
    --icon-bg: #f4fbe9;
  }
  * { box-sizing: border-box; margin: 0; padding: 0; }
  html, body {
    width: 1200px; height: 800px; overflow: hidden;
    background: var(--backdrop);
    font-family: "Lato", sans-serif;
  }
  .stage { position: relative; width: 1200px; height: 800px; }

  .card {
    position: absolute;
    background: linear-gradient(135deg, #15201d 0%, var(--card-dark) 55%, var(--card-dark-edge) 100%);
    box-shadow: 0 14px 30px rgba(0,0,0,0.28);
  }

  /* Front: portrait */
  .card-front {
    left: 90px; top: 120px; width: 420px; height: 560px;
  }
  .strand-art {
    position: absolute; left: 26px; top: 14px; width: 110px; height: 532px;
    border-radius: 30px;
    background: linear-gradient(180deg,
      var(--strand-grey) 0%, var(--strand-grey) 28%,
      var(--strand-green) 40%, var(--brand-green) 55%,
      var(--strand-grey) 70%, var(--strand-grey) 100%);
    opacity: 0.55;
  }
  .brand-name {
    position: absolute; left: 150px; top: 250px;
    font-weight: 400; font-size: 38px; letter-spacing: -0.5px;
    color: var(--brand-green); white-space: nowrap;
  }

  /* Back: landscape */
  .card-back {
    left: 560px; top: 228px; width: 600px; height: 343px;
  }
  .back-shapes { position: absolute; left: 0; top: 0; }
  .name-block {
    position: absolute; left: 92px; top: 80px; width: 170px;
    color: var(--ink);
  }
  .person-name { font-weight: 700; font-size: 17px; }
  .person-role { font-weight: 400; font-size: 12px; margin-top: 3px; }

  .contact-list {
    position: absolute; right: 120px; top: 134px;
    list-style: none; color: var(--ink);
    font-size: 14px; line-height: 1;
  }
  .contact-list li {
    display: flex; justify-content: flex-end; align-items: center;
    gap: 8px; margin-bottom: 11px; white-space: nowrap;
  }
  .contact-icon {
    width: 15px; height: 15px; border-radius: 50%;
    background: var(--icon-bg); flex: none;
    display: flex; align-items: center; justify-content: center;
  }
</style>
</head>
<body>
<main class="stage">

  <section class="card card-front" aria-label="Business card front">
    <div class="strand-art" role="img" aria-label="Vertical DNA strand illustration in grey and green"></div>
    <span class="brand-name">LUMEN CELL</span>
  </section>

  <section class="card card-back" aria-label="Business card back">
    <svg class="back-shapes" width="600" height="343" viewBox="0 0 600 343" aria-hidden="true">
      <defs>
        <linearGradient id="nameFill" x1="0" y1="0" x2="1" y2="1">
          <stop offset="0" stop-color="#2bb878"/>
          <stop offset="1" stop-color="#22a86a"/>
        </linearGradient>
        <linearGradient id="contactFill" x1="0" y1="0" x2="1" y2="1">
          <stop offset="0" stop-color="#a6d972"/>
          <stop offset="1" stop-color="#55a62a"/>
        </linearGradient>
      </defs>
      <circle cx="165" cy="118" r="98" fill="url(#nameFill)"/>
      <rect x="285" y="100" width="170" height="95" rx="47" fill="url(#contactFill)"/>
      <circle cx="440" cy="205" r="125" fill="url(#contactFill)"/>
    </svg>

    <div class="name-block">
      <p class="person-name">Dr. Aaro Lind</p>
      <p class="person-role">Head Scientist</p>
    </div>

    <ul class="contact-list">
      <li>+000 555 0142
        <span class="contact-icon">
          <svg width="9" height="9" viewBox="0 0 10 10"><path d="M2 1l2 2-1 1.3c.6 1.2 1.5 2.1 2.7 2.7L7 6l2 2-1.3 1.3C4.5 9 1 5.5.7 2.3z" fill="#55a62a"/></svg>
        </span>
      </li>
      <li>aaro.lind@lumencell.com
        <span class="contact-icon">
          <svg width="9" height="9" viewBox="0 0 10 10"><rect x="1" y="2.5" width="8" height="5.5" fill="none" stroke="#55a62a" stroke-width="1.2"/><path d="M1 2.5l4 3 4-3" fill="none" stroke="#55a62a" stroke-width="1.2"/></svg>
        </span>
      </li>
      <li>www.lumencell.com
        <span class="contact-icon">
          <svg width="10" height="10" viewBox="0 0 10 10"><circle cx="5" cy="5" r="4" fill="none" stroke="#55a62a" stroke-width="1"/><path d="M1 5h8M5 1v8M2 3h6M2 7h6" stroke="#55a62a" stroke-width="0.8"/></svg>
        </span>
      </li>
    </ul>
  </section>

</main>
</body>
</html>
```